stationary deign for trucking company

im a trucking company looking for a professional set of stationary designs i deliver goods from point a to b
Updates

When submitting stationary designs I need envelope design, letterhead, cards, I’d badge etc

Industry/Entity Type

Trucking Company

Requirements
Must have
• must have letter head, business card, envelope, fax sheet, id badge, folder, thank you card, notebook, invoice sheet.
Nice to have
• nice to have them all custom made (letterhead,envelope, business card, I’d badge etc
Should not have
• must not have prepaid sign want i unique design for items

```html
<!DOCTYPE html>
<html lang="en">
<head>
<meta charset="utf-8">
<title>Halbrook Freight + Logistics – Presentation Folder</title>
<link rel="stylesheet" href="https://fonts.googleapis.com/css2?family=Montserrat:wght@500&display=swap">
<style>
  :root {
    --brand-blue: #1a5aa8;
    --band-grey: #d3d3d3;
    --paper: #ffffff;
    --ink: #1e1e1e;
    --sky-top: #1f78c0;
    --sky-mid: #8fb8dc;
    --road-dark: #3a3f4a;
    --shadow: rgba(0, 0, 0, 0.28);
  }
  html, body {
    margin: 0;
    width: 1200px;
    height: 1200px;
    overflow: hidden;
    background: var(--paper);
  }
  .folder-sheet {
    display: block;
    width: 1200px;
    height: 1200px;
  }
  .brand-text {
    font-family: "Montserrat", sans-serif;
    font-weight: 500;
    fill: var(--ink);
  }
  .contact-text {
    font-family: "Montserrat", sans-serif;
    font-weight: 500;
    font-size: 7.5px;
    fill: var(--paper);
  }
</style>
</head>
<body>
<svg class="folder-sheet" viewBox="0 0 1200 1200" xmlns="http://www.w3.org/2000/svg">
  <defs>
    <filter id="panel-shadow" x="-10%" y="-10%" width="130%" height="130%">
      <feDropShadow dx="14" dy="14" stdDeviation="10" flood-color="#000" flood-opacity="0.28"/>
    </filter>
    <linearGradient id="highway-tones" x1="0" y1="0" x2="0" y2="1">
      <stop offset="0" stop-color="var(--sky-top)"/>
      <stop offset="0.45" stop-color="var(--sky-mid)"/>
      <stop offset="0.7" stop-color="#2f4f8a"/>
      <stop offset="1" stop-color="var(--road-dark)"/>
    </linearGradient>
  </defs>

  <!-- Outer spread: back cover + front cover -->
  <g class="outer-spread" filter="url(#panel-shadow)">
    <rect class="spread-base" x="178" y="22" width="844" height="552" fill="var(--paper)"/>
  </g>

  <g class="back-cover">
    <rect x="178" y="22" width="422" height="552" fill="var(--brand-blue)"/>
    <rect class="back-stripe" x="178" y="551" width="422" height="14" fill="var(--paper)"/>
    <g class="contact-block" text-anchor="middle">
      <text class="contact-text" x="389" y="499">YOUR ADDRESS HERE</text>
      <text class="contact-text" x="389" y="508">12345</text>
      <text class="contact-text" x="389" y="522">000111222</text>
      <text class="contact-text" x="389" y="533">info@halbrookfreight.com</text>
      <text class="contact-text" x="389" y="544">halbrookfreight.com</text>
    </g>
  </g>

  <g class="front-cover">
    <rect x="600" y="22" width="422" height="552" fill="var(--paper)"/>
    <rect class="cover-photo" x="667" y="22" width="287" height="552" fill="url(#highway-tones)"
          role="img" aria-label="Photograph of trucks speeding along a highway at dusk"/>
    <rect class="brand-band" x="600" y="64" width="422" height="59" fill="var(--band-grey)"/>
    <g class="brand-lockup">
      <rect x="724" y="82" width="22" height="22" fill="var(--brand-blue)"/>
      <text class="brand-text" x="768" y="97" font-size="19" letter-spacing="2">HALBROOK</text>
      <text class="brand-text" x="769" y="106" font-size="6" letter-spacing="1.2">FREIGHT + LOGISTICS</text>
    </g>
  </g>

  <!-- Inside spread: pockets -->
  <g class="inside-spread" filter="url(#panel-shadow)">
    <rect x="178" y="625" width="844" height="552" fill="var(--band-grey)"/>
  </g>
  <g class="inside-pockets">
    <line class="fold-line" x1="600" y1="625" x2="600" y2="1177" stroke="var(--paper)" stroke-width="1.5"/>
    <polygon class="pocket-left" points="178,983 482,983 600,1177 178,1177" fill="var(--brand-blue)"/>
    <polygon class="pocket-right" points="1022,983 718,983 600,1177 1022,1177" fill="var(--brand-blue)"/>
  </g>
</svg>
</body>
</html>
```